New business card design to go with our new logo

just want an eye-catching business card to go with our new logo. We are open to double sided or single sided. Just want it to have the following info on it. Whatever layout you think looks best.

First and Last Name
Title
Phone 801-555-0187
Address 312 W. Larkmoor Avenue Orem UT 84057
Email thecrew@meadowstailandkennel.example

Industry/Entity Type

Business

```html
<!DOCTYPE html>
<html lang="en">
<head>
<meta charset="utf-8">
<title>Meadow's Tail &amp; Kennel — Business Card</title>
<link rel="stylesheet" href="https://fonts.googleapis.com/css2?family=Open+Sans:wght@400;600&display=swap">
<style>
  :root {
    --page-bg: #1d1e20;
    --card-blue: #2aa3d3;
    --card-clear: #34373b;
    --accent-orange: #e8833a;
    --text-light: #f4f8fb;
    --logo-blue: #2c8fb8;
  }
  * { margin: 0; padding: 0; box-sizing: border-box; }
  html, body {
    width: 1200px; height: 1200px; overflow: hidden;
    background: var(--page-bg);
    font-family: "Open Sans", Arial, sans-serif;
  }
  .card {
    position: absolute;
    left: 100px; top: 315px;
    width: 1000px; height: 570px;
    border-radius: 0 28px 28px 0;
    overflow: hidden;
    box-shadow: 0 20px 50px rgba(0,0,0,.55);
  }
  .card-shapes { position: absolute; inset: 0; }
  .contact {
    position: absolute; left: 70px; top: 170px;
    color: var(--text-light);
  }
  .contact-name { font-size: 40px; font-weight: 600; letter-spacing: .5px; }
  .contact-title { font-size: 21px; margin-top: 2px; }
  .contact-list { list-style: none; margin-top: 30px; font-size: 21px; }
  .contact-list li { display: flex; align-items: center; gap: 14px; margin-bottom: 8px; }
  .contact-list svg { width: 20px; height: 20px; flex: none; }
  .contact-divider { height: 1px; background: rgba(255,255,255,.7); width: 440px; margin: 10px 0 14px; }
  .brand {
    position: absolute; left: 640px; top: 200px; width: 320px;
    display: flex; flex-direction: column; align-items: center; gap: 18px;
  }
  .brand-mark {
    width: 110px; height: 110px; border-radius: 50%;
    border: 6px solid var(--accent-orange);
  }
  .brand-name {
    font-size: 32px; font-weight: 600; color: var(--accent-orange);
    text-align: center; line-height: 1.2;
  }
</style>
</head>
<body>
  <article class="card">
    <svg class="card-shapes" viewBox="0 0 1000 570" width="1000" height="570">
      <rect class="card-blue-field" width="1000" height="570" fill="var(--card-blue)"/>
      <path class="card-orange-arc" d="M445,0 C445,330 690,492 1000,480 L1000,456 C700,466 480,320 478,0 Z" fill="var(--accent-orange)"/>
      <path class="card-clear-panel" d="M478,0 C480,320 700,466 1000,456 L1000,0 Z" fill="var(--card-clear)"/>
    </svg>

    <section class="contact">
      <h1 class="contact-name">JOHN DOE</h1>
      <p class="contact-title">Director</p>
      <ul class="contact-list">
        <li>
          <svg viewBox="0 0 24 24" aria-hidden="true"><path fill="var(--text-light)" d="M3 9c0-3 4-5 9-5s9 2 9 5l-4 1-1-3H8L7 10 3 9zm4 3h10l2 8H5l2-8zm5 2a2.5 2.5 0 100 5 2.5 2.5 0 000-5z"/></svg>
          801-555-0187
        </li>
        <li>
          <svg viewBox="0 0 24 24" aria-hidden="true"><rect x="2" y="5" width="20" height="14" fill="var(--text-light)"/><path d="M2 5l10 8 10-8" fill="none" stroke="var(--card-blue)" stroke-width="2"/></svg>
          thecrew@meadowstailandkennel.example
        </li>
      </ul>
      <div class="contact-divider"></div>
      <ul class="contact-list" style="margin-top:0">
        <li>
          <svg viewBox="0 0 24 24" aria-hidden="true"><path fill="var(--text-light)" d="M12 2a7 7 0 00-7 7c0 5 7 13 7 13s7-8 7-13a7 7 0 00-7-7zm0 9.5A2.5 2.5 0 1112 6.5a2.5 2.5 0 010 5z"/></svg>
          312 W. Larkmoor Avenue Orem UT 84057
        </li>
      </ul>
    </section>

    <div class="brand">
      <div class="brand-mark"></div>
      <p class="brand-name">Meadow's Tail &amp; Kennel</p>
    </div>
  </article>
</body>
</html>
```